Design a Brazilian children's Bible calendar for 2017

We need someone to design a children's calendar for 2017 with an animal theme.
The format is 21cm x 15cm and we need the front cover and one page with two months as can be seen in the attached files.
Target Market(s)
Brazilian children
Font styles to use
Sans Serif
Requirements
Must have
- Modern, clean design

```html
<!DOCTYPE html>
<html lang="pt-BR">
<head>
<meta charset="UTF-8">
<title>Calendário 2017 – Maio e Junho</title>
<link rel="stylesheet" href="https://fonts.googleapis.com/css2?family=Raleway:wght@500;700&family=Quicksand:wght@400;500&family=Fredoka:wght@600&display=swap">
<style>
  :root {
    --sun: #f6c555;
    --white: #ffffff;
    --brick: #a5472c;
    --label-brown: #8a4a2c;
    --leaf-deep: #2f6b3a;
    --leaf-mid: #4f8a4a;
    --sky-haze: #c9d3c4;
    --fur: #8a6a4a;
  }
  * { margin: 0; padding: 0; box-sizing: border-box; }
  html, body { width: 856px; height: 1200px; overflow: hidden; background: var(--sun); }
  .calendar-page { position: relative; width: 856px; height: 1200px; background: var(--sun); overflow: hidden; }

  .cover-photo {
    position: absolute; left: 0; top: 0; width: 856px; height: 600px;
    background:
      radial-gradient(ellipse 260px 420px at 300px 420px, var(--fur) 0%, rgba(138,106,74,0) 70%),
      linear-gradient(180deg, var(--sky-haze) 0%, var(--leaf-mid) 18%, var(--leaf-deep) 70%, #2a5a30 100%);
  }
  .cover-quote {
    position: absolute; right: 71px; top: 378px; text-align: right;
    font-family: "Raleway", sans-serif; font-weight: 500; color: var(--white);
    font-size: 33px; line-height: 37px;
  }
  .cover-quote-source {
    position: absolute; right: 71px; top: 545px;
    font-family: "Raleway", sans-serif; font-weight: 700; color: var(--white);
    font-size: 17px; letter-spacing: 0.3px;
  }

  .season-scene {
    position: absolute; left: 77px; top: 619px; width: 706px; height: 188px;
    background: linear-gradient(180deg, rgba(242,140,40,0) 0%, rgba(242,140,40,0.18) 60%, rgba(108,150,40,0.35) 100%);
    border-radius: 90px 90px 0 0;
  }
  .year {
    position: absolute; left: 343px; top: 728px;
    font-family: "Fredoka", sans-serif; font-weight: 600; font-size: 52px;
    color: var(--brick); line-height: 1;
  }

  .month { position: absolute; top: 810px; width: 332px; }
  .month-may { left: 63px; }
  .month-june { left: 461px; }
  .month-name {
    text-align: center; font-family: "Quicksand", sans-serif; font-weight: 400;
    font-size: 44px; color: var(--white); line-height: 1; height: 70px;
  }
  .month-may .month-name { padding-right: 0; transform: translateX(-11px); }
  .month-june .month-name { transform: translateX(17px); }

  .weekdays, .days { display: grid; grid-template-columns: repeat(7, 47.4px); }
  .weekdays span {
    width: 42px; height: 42px; border-radius: 50%; background: var(--white);
    display: flex; align-items: center; justify-content: center;
    font-family: "Raleway", sans-serif; font-weight: 700; font-size: 13px;
    color: var(--label-brown);
  }
  .days { margin-top: 18px; grid-auto-rows: 36px; }
  .days span {
    width: 42px; text-align: center; font-family: "Quicksand", sans-serif;
    font-weight: 500; font-size: 25px; color: var(--white); line-height: 36px;
  }
</style>
</head>
<body>
<div class="calendar-page">
  <div class="cover-photo" role="img" aria-label="Fotografia de uma girafa diante de árvores verdes"></div>
  <p class="cover-quote">Lorem<br>ipsum dolor sit<br>amet czonsectetuer<br>adipiscing elit aenean</p>
  <p class="cover-quote-source">LOREM IPSUM</p>

  <div class="season-scene" role="img" aria-label="Ilustração de nuvens, arbustos, pássaros e uma girafa comendo folhas"></div>
  <div class="year">2017</div>

  <section class="month month-may">
    <h2 class="month-name">Maio</h2>
    <div class="weekdays"><span>DOM</span><span>TER</span><span>QUA</span><span>QUI</span><span>QUI</span><span>SEX</span><span>SÁB</span></div>
    <div class="days">
      <span></span><span>1</span><span>2</span><span>3</span><span>4</span><span>5</span><span>6</span>
      <span>7</span><span>8</span><span>9</span><span>10</span><span>11</span><span>12</span><span>13</span>
      <span>14</span><span>15</span><span>16</span><span>17</span><span>18</span><span>19</span><span>20</span>
      <span>21</span><span>22</span><span>23</span><span>24</span><span>25</span><span>26</span><span>27</span>
      <span>28</span><span>29</span><span>30</span><span>31</span>
    </div>
  </section>

  <section class="month month-june">
    <h2 class="month-name">Junho</h2>
    <div class="weekdays"><span>DOM</span><span>TER</span><span>QUA</span><span>QUI</span><span>QUI</span><span>SEX</span><span>SÁB</span></div>
    <div class="days">
      <span></span><span></span><span></span><span></span><span>1</span><span>2</span><span>3</span>
      <span>4</span><span>5</span><span>6</span><span>7</span><span>8</span><span>9</span><span>10</span>
      <span>11</span><span>12</span><span>13</span><span>14</span><span>15</span><span>16</span><span>17</span>
      <span>18</span><span>19</span><span>20</span><span>21</span><span>22</span><span>23</span><span>24</span>
      <span>25</span><span>26</span><span>27</span><span>28</span><span>29</span><span>30</span>
    </div>
  </section>
</div>
</body>
</html>
```